Premium wine label refresh for Harbor &Vane wines

Our Harbor & Vane label is dated. We're looking for a contemporary refresh that will stand out on the shelf, make a strong quality statement and a more contemporary look. Feel free to take a completely fresh approach but the label should connect with the brand story. Harbor & Vane refers to my convict ancestry and is a tribute to humble beginnings. Where we finish is not necessarily where we start.

Refer to the attached PDF file for a detailed brief.

Target Market(s)

Aspirational, educated wine drinkers 30-55

Industry/Entity Type

Wine

Font styles to use
Sans Serif

Requirements
Must have
• Shelf presence, premium feel, connection to the existing label
Nice to have
• Print quality cues like embossing, foil etc.
Should not have
• Fun look and feel.

```html
<!DOCTYPE html>
<html lang="en">
<head>
<meta charset="utf-8">
<title>Design Notes – Tallowby logo and Harbor &amp; Vane Range</title>
<link rel="stylesheet" href="https://fonts.googleapis.com/css2?family=Open+Sans:ital,wght@0,400;0,600;0,700;1,400&family=Playfair+Display:wght@400;600&family=Josefin+Sans:wght@300;400&display=swap">
<style>
  :root {
    --ink: #111111;
    --paper: #ffffff;
    --label-cream: #efebe3;
    --label-panel: #f3f0ea;
    --sketch-soft: #dccdc2;
    --wine-red: #7b1e2c;
    --band-black: #000000;
    --band-grey: #c4c4c4;
    --copper: #c98a62;
    --rule-grey: #c8c8c8;
  }
  * { box-sizing: border-box; margin: 0; padding: 0; }
  html, body { width: 1200px; height: 1000px; overflow: hidden; background: var(--paper); }
  body { position: relative; font-family: "Open Sans", Arial, sans-serif; color: var(--ink); }
  .abs { position: absolute; }

  .board-title { left: 51px; top: 46px; font-size: 29px; font-weight: 400; letter-spacing: -0.2px; }

  /* Label */
  .label { left: 51px; top: 106px; width: 603px; height: 574px; background: var(--label-cream); overflow: hidden; }
  .label-art-jump { left: 449px; top: 9px; width: 146px; height: 258px; border-radius: 40px;
    background: radial-gradient(ellipse at 50% 45%, var(--sketch-soft), rgba(220,205,194,0) 70%); }
  .label-art-dig { left: 21px; top: 284px; width: 186px; height: 210px; border-radius: 40px;
    background: radial-gradient(ellipse at 45% 55%, var(--sketch-soft), rgba(220,205,194,0) 70%); }
  .label-region { left: 0; width: 603px; top: 42px; text-align: center; font-family: "Josefin Sans", sans-serif;
    font-weight: 400; font-size: 26px; letter-spacing: 2px; color: #55514c; }
  .label-range { left: 0; width: 603px; top: 80px; text-align: center; font-family: "Josefin Sans", sans-serif;
    font-weight: 300; font-size: 31px; letter-spacing: 3px; color: #3f3b37; }
  .label-centre { left: 225px; top: 137px; width: 152px; height: 232px; background: var(--label-panel);
    box-shadow: 0 0 0 1px rgba(0,0,0,0.04), inset 0 0 6px rgba(0,0,0,0.05);
    display: flex; align-items: center; justify-content: center; }
  .centre-name { font-family: "Josefin Sans", sans-serif; font-weight: 400; font-size: 15px; letter-spacing: 2px;
    line-height: 22px; color: var(--copper); text-align: center; }
  .label-variety { left: 0; width: 603px; top: 396px; text-align: center; font-family: "Playfair Display", serif;
    font-weight: 600; font-size: 22px; letter-spacing: 1px; color: var(--wine-red); }
  .label-vintage { left: 0; width: 603px; top: 434px; text-align: center; font-family: "Josefin Sans", sans-serif;
    font-size: 22px; color: var(--ink); }
  .label-band { left: 0; top: 503px; width: 603px; height: 71px; background: var(--band-black);
    display: flex; align-items: center; justify-content: center; }
  .band-name { font-family: "Playfair Display", serif; font-weight: 400; font-size: 20px; letter-spacing: 3px; color: var(--band-grey); }

  .leader { stroke: var(--rule-grey); stroke-width: 0.8; }

  /* Notes */
  .notes { left: 718px; top: 100px; width: 445px; font-size: 17px; line-height: 21.5px; }
  .notes h2 { font-size: 17.5px; font-weight: 600; margin-bottom: 8px; }
  .notes ol { list-style: none; }
  .notes li { position: relative; padding-left: 18px; margin-bottom: 2px; }
  .notes .num { position: absolute; left: 0; font-weight: 700; }
  .notes b { font-weight: 700; }
  .notes em { font-style: italic; }

  .foil-card { left: 737px; top: 505px; width: 191px; height: 192px; background: var(--label-panel);
    display: flex; align-items: center; justify-content: center; }
  .foil-name { font-family: "Josefin Sans", sans-serif; font-size: 18px; letter-spacing: 1.5px; color: var(--copper); text-align: center; line-height: 24px; }

  .swatch { top: 505px; width: 36px; height: 69px; }
  .swatch-caption { top: 580px; font-size: 10px; width: 50px; text-align: center; }
  .closure-note { left: 962px; top: 597px; width: 180px; font-size: 14px; line-height: 16.8px; }
  .closure-note b { font-weight: 600; }

  /* Logo cleanup */
  .cleanup-note { left: 50px; top: 712px; width: 250px; font-size: 16.5px; line-height: 19.3px; }
  .cleanup-note h3 { font-size: 16.5px; font-weight: 600; margin-bottom: 5px; }
  .cleanup-note p { margin-bottom: 5px; }

  .logo-dark { left: 314px; top: 718px; width: 267px; height: 231px; background: var(--band-black); }
  .logo-light { left: 596px; top: 770px; width: 160px; height: 130px; }
  .wordmark { position: absolute; left: 0; width: 100%; text-align: center; font-family: "Playfair Display", serif; font-weight: 400; letter-spacing: 2px; }
  .sub-wordmark { position: absolute; left: 0; width: 100%; text-align: center; font-family: "Josefin Sans", sans-serif; letter-spacing: 3px; }

  .existing-caption { left: 808px; top: 810px; width: 129px; text-align: center; font-size: 13px; }
  .logo-existing { left: 808px; top: 836px; width: 129px; height: 113px; background: var(--band-black); }

  .sketch-pencil { left: 1005px; top: 740px; width: 175px; height: 92px; border-radius: 30px;
    background: radial-gradient(ellipse at 50% 50%, #e8e8e8, rgba(232,232,232,0) 72%); }
  .sketch-ink { left: 1000px; top: 855px; width: 182px; height: 98px; border-radius: 30px;
    background: radial-gradient(ellipse at 50% 55%, #8a8a8a, rgba(138,138,138,0) 72%); }
</style>
</head>
<body>

<h1 class="abs board-title">Design Notes_Tallowby logo and Harbor &amp; Vane Range</h1>

<section class="abs label" aria-label="Harbor &amp; Vane wine label">
  <div class="abs label-art-jump" role="img" aria-label="Sepia pencil sketch of a man leaping in celebration over topographic contour lines"></div>
  <div class="abs label-art-dig" role="img" aria-label="Sepia pencil sketch of a labourer digging the earth with a shovel"></div>
  <div class="abs label-region">HIGHFIELDS</div>
  <div class="abs label-range">HARBOR &amp; VANE</div>
  <div class="abs label-centre"><div class="centre-name">HARBOR<br>&amp; VANE</div></div>
  <div class="abs label-variety">CABERNET SAUVIGNON</div>
  <div class="abs label-vintage">2022</div>
  <div class="abs label-band"><span class="band-name">TALLOWBY VINEYARDS</span></div>
</section>

<svg class="abs" style="left:0;top:0" width="1200" height="1000" aria-hidden="true">
  <line class="leader" x1="650" y1="141" x2="710" y2="141"/>
  <line class="leader" x1="641" y1="253" x2="710" y2="253"/>
  <line class="leader" x1="422" y1="388" x2="710" y2="388"/>
</svg>

<section class="abs notes">
  <h2>Making your wine stand out on the shelf:</h2>
  <ol>
    <li><span class="num">1.</span><b>Tell a story.</b> Harbor &amp; Vane has a great story - the images bring attention to this.<br>
      <em>Nice to have: These are my drawings, but you may ask a local artist to do similar, adding a local, personalised touch to your story.</em></li>
    <li><span class="num">2.</span><b>Textured label paper.</b>&nbsp; This print gives an embossed look, but would be great to have the label embossed so that customer can <b>feel</b> the <b>connection to the earth</b> (topographic lines) when they pick the bottle up.&nbsp; The earth also <b>connects the past and present</b> in the story.The centre square is block pressed (stamped into the paper) to form a calm centre.</li>
    <li><span class="num">3.</span><b>Simplicity.</b> The name and image of harbor &amp; vane are best displayed in minimalist style.</li>
    <li><span class="num">4.</span><b>Optional hot foil emboss</b> (copper) on the key only.</li>
  </ol>
</section>

<div class="abs foil-card"><div class="foil-name">HARBOR<br>&amp; VANE</div></div>

<svg class="abs swatch" style="left:962px" viewBox="0 0 36 69" role="img" aria-label="Reds colourway"><rect width="36" height="69" fill="#1b1b1b"/></svg>
<svg class="abs swatch" style="left:1005px" viewBox="0 0 36 69" role="img" aria-label="Rosé colourway"><rect width="36" height="69" fill="#262626"/></svg>
<svg class="abs swatch" style="left:1055px" viewBox="0 0 36 69" role="img" aria-label="Whites colourway"><rect width="36" height="69" fill="#f0ece4"/></svg>
<svg class="abs swatch" style="left:1113px" viewBox="0 0 36 69" role="img" aria-label="Copper closure colourway"><rect width="36" height="69" fill="#8f6653"/></svg>
<div class="abs swatch-caption" style="left:955px">Reds</div>
<div class="abs swatch-caption" style="left:998px">Rosé</div>
<div class="abs swatch-caption" style="left:1048px">Whites</div>

<p class="abs closure-note"><b>Bottle closure.</b> I wanted to use toffee or copper from the standard range to match the sketches, but it looks like you have used it on another range.</p>

<section class="abs cleanup-note">
  <h3>Logo Cleanup</h3>
  <p>I love your logo and the Tallowby font (Playfair Display). Its a gorgeous modern transitional font and is classic yet trendy - perfect for wine.</p>
  <p>So I have kept it, but updated the Vineyards text to Oscar, a very cutting edge look and feel.&nbsp; Logo mark has been modernised.</p>
</section>

<div class="abs logo-dark">
  <svg class="abs" style="left:113px;top:60px" width="40" height="40" aria-hidden="true"><circle cx="20" cy="20" r="18" fill="var(--band-grey)"/></svg>
  <div class="wordmark" style="top:122px;font-size:38px;color:var(--band-grey)">TALLOWBY</div>
  <div class="sub-wordmark" style="top:178px;font-size:15px;color:var(--band-grey)">VINEYARDS</div>
</div>

<div class="abs logo-light">
  <svg class="abs" style="left:65px;top:10px" width="30" height="30" aria-hidden="true"><circle cx="15" cy="15" r="13" fill="#9e9e9e"/></svg>
  <div class="wordmark" style="top:64px;font-size:27px;color:var(--ink)">TALLOWBY</div>
  <div class="sub-wordmark" style="top:106px;font-size:11px;color:var(--ink)">VINEYARDS</div>
</div>

<div class="abs existing-caption">Existing logo</div>
<div class="abs logo-existing">
  <div class="wordmark" style="top:44px;font-size:17px;color:#e6e6e6;letter-spacing:1px">TALLOWBY<br>VINEYARDS</div>
</div>

<div class="abs sketch-pencil" role="img" aria-label="Light pencil studies of the digging labourer and a standing figure with arms outstretched"></div>
<div class="abs sketch-ink" role="img" aria-label="Black ink studies of the digging labourer and a figure raising a bunch of grapes"></div>

</body>
</html>
```